Business Cards for our company

Hi there,

we have successfully designed a logo with ArtFlock and would like now to design our business cards. We would like to keep the colours and the look-and-feel of the logo. Please send in variations with two or three colours and one or two sides. I promise to respond to every single submission.

Many thanks and happy new year.

All the best,
Wilfried

Target Market(s)

B2B

Industry/Entity Type

Trade

Contact Information for Business Card

We have successfully designed a logo with ArtFlock and would like now to design our business cards. We would like to keep the colours and the look-and-feel of the logo. Please send in variations with two or three colours and one or two sides. I promise to respond to every single submission.

Font styles to use
Serif
Sans Serif
Script

Requirements
Must have
• These information should be on the business card, grouped as you suggest, and we think using small pictograms for mobile, email, etc is pretty helpful:
• Wilfried Tammler (first and second name)
• Geschäftsführer/ Managing Director (title)
• KoR Warenkontor GmbH (company name and legal form)
• Ostheimer Str. 18/3 (street and house number)
• 73412 Feldbrunn (zip code and town)
• +491709384562 (mobile)
• +4940569027341 (work)
• w.tammler@kor-warenkontor.example (email)
• www.kor-warenkontor.example (web)
Nice to have
• Spectacular and interesting layout and design. You look at it and think, wow, that's not the normal stuff.
• We think of ourselves as bridge-builders between businesses (international producers on the one hand, and retail chains on the other hand) and we translate, organise and manage projects where both partners are involved, but it's difficult for them to cooperate due to language barriers and different working cultures.
• This is why we have the n between the B's shaped as a bridge, and the green arc supports this idea. Maybe you could play with this idea...
Should not have
• the standard layout that everybody has

```html
<!DOCTYPE html>
<html lang="de">
<head>
<meta charset="utf-8">
<title>KoR Warenkontor GmbH – Visitenkarte</title>
<link rel="stylesheet" href="https://fonts.googleapis.com/css2?family=Open+Sans:wght@400;600;700;800&display=swap">
<style>
  :root {
    --stage: #1d1d1d;
    --card-light: #e6e3dd;
    --card-mid: #cfcbc4;
    --card-shade: #b9b5ae;
    --green: #1fa64a;
    --ink: #1b1b1b;
    --ink-soft: #3a3a3a;
    --white: #ffffff;
  }
  * { box-sizing: border-box; margin: 0; padding: 0; }
  html, body {
    width: 1200px; height: 737px; overflow: hidden;
    background: var(--stage);
    font-family: "Open Sans", Arial, sans-serif;
  }
  .card {
    position: absolute; left: 150px; top: 78px;
    width: 900px; height: 580px; overflow: hidden;
    background: var(--card-light);
  }
  .card__backdrop {
    position: absolute; inset: 0;
    background:
      radial-gradient(ellipse at 50% 75%, rgba(255,255,255,0.55), rgba(255,255,255,0) 60%),
      linear-gradient(180deg, var(--card-mid) 0%, var(--card-light) 45%, var(--card-shade) 100%);
  }
  .card__graphics { position: absolute; inset: 0; }
  .brand {
    position: absolute; left: 340px; top: 70px; width: 320px;
    display: flex; align-items: center; justify-content: center; gap: 18px;
  }
  .brand__dot {
    width: 26px; height: 26px; border-radius: 50%; background: var(--green);
  }
  .brand__name {
    font-size: 96px; font-weight: 800; color: var(--ink); letter-spacing: 2px; line-height: 1;
  }
  .company-tab {
    position: absolute; left: 300px; top: 238px; width: 380px;
    text-align: center; color: var(--white);
    font-size: 26px; font-weight: 400; line-height: 40px;
  }
  .person {
    position: absolute; left: 90px; top: 355px; text-align: right; width: 330px;
  }
  .person__name {
    font-size: 30px; font-weight: 800; color: var(--ink); text-transform: uppercase;
    letter-spacing: 0.5px;
  }
  .person__title {
    font-size: 15px; font-weight: 600; color: var(--ink-soft); margin-top: 2px;
  }
  .contact {
    position: absolute; left: 500px; top: 306px; list-style: none;
  }
  .contact__item {
    display: flex; align-items: flex-start; gap: 14px;
    font-size: 15px; color: var(--ink-soft); line-height: 19px;
    margin-bottom: 11px;
  }
  .contact__icon { flex: none; width: 24px; height: 24px; }
</style>
</head>
<body>
  <article class="card">
    <div class="card__backdrop" role="img" aria-label="Soft, faded photograph of a bridge walkway in light grey tones"></div>

    <svg class="card__graphics" viewBox="0 0 900 580" width="900" height="580" aria-hidden="true">
      <polygon points="0,222 900,262 900,270 0,230" fill="var(--green)"/>
      <polygon points="270,236 700,255 668,290 300,276" fill="var(--green)"/>
      <line x1="470" y1="330" x2="470" y2="470" stroke="var(--green)" stroke-width="2"/>
    </svg>

    <div class="brand">
      <span class="brand__name">KoR</span>
      <span class="brand__dot"></span>
    </div>

    <div class="company-tab">KoR Warenkontor GmbH</div>

    <div class="person">
      <p class="person__name">Wilfried Tammler</p>
      <p class="person__title">Geschäftsführer/ Managing Director</p>
    </div>

    <ul class="contact">
      <li class="contact__item">
        <svg class="contact__icon" viewBox="0 0 24 24"><circle cx="12" cy="12" r="12" fill="var(--green)"/><path d="M12 5a4.5 4.5 0 0 0-4.5 4.5c0 3.4 4.5 8.5 4.5 8.5s4.5-5.1 4.5-8.5A4.5 4.5 0 0 0 12 5z" fill="#fff"/><circle cx="12" cy="9.5" r="1.7" fill="var(--green)"/></svg>
        <span>Ostheimer Str. 18/3<br>73412 Feldbrunn</span>
      </li>
      <li class="contact__item">
        <svg class="contact__icon" viewBox="0 0 24 24"><circle cx="12" cy="12" r="12" fill="var(--green)"/><rect x="8.5" y="5" width="7" height="14" rx="1.5" fill="#fff"/><rect x="9.8" y="7" width="4.4" height="8" fill="var(--green)"/></svg>
        <span>+491709384562</span>
      </li>
      <li class="contact__item">
        <svg class="contact__icon" viewBox="0 0 24 24"><circle cx="12" cy="12" r="12" fill="var(--green)"/><path d="M8 6.5l2.3-.5 1.3 3-1.5 1.2a7.5 7.5 0 0 0 3.7 3.7l1.2-1.5 3 1.3-.5 2.3c-5.3.6-10.1-4.2-9.5-9.5z" fill="#fff"/></svg>
        <span>+4940569027341</span>
      </li>
      <li class="contact__item">
        <svg class="contact__icon" viewBox="0 0 24 24"><circle cx="12" cy="12" r="12" fill="var(--green)"/><rect x="6" y="8" width="12" height="8.5" rx="1" fill="#fff"/><path d="M6.5 8.5l5.5 4.2 5.5-4.2" fill="none" stroke="var(--green)" stroke-width="1.2"/></svg>
        <span>w.tammler@kor-warenkontor.example</span>
      </li>
      <li class="contact__item">
        <svg class="contact__icon" viewBox="0 0 24 24"><circle cx="12" cy="12" r="12" fill="var(--green)"/><circle cx="12" cy="12" r="6" fill="none" stroke="#fff" stroke-width="1.4"/><ellipse cx="12" cy="12" rx="2.6" ry="6" fill="none" stroke="#fff" stroke-width="1.2"/><line x1="6" y1="12" x2="18" y2="12" stroke="#fff" stroke-width="1.2"/></svg>
        <span>www.kor-warenkontor.example</span>
      </li>
    </ul>
  </article>
</body>
</html>
```